Web Design - 1 page for Buy - Repair - Service - Upgrade - PC Maintenance

We specialize in consumer and small business. It will be mobile friendly, viewable on all devices. Fully editable at the text level of the sections !!! - HTML / CSS only to be able to add a section would be to the web site
Updates

Target Market(s)

consumer and small business IT.

Coding

Coded - Design and coding required

Number of Pages Required

1 page

Font styles to use
Sans Serif

Requirements
Must have
• Looking for a page with a design that compliments the business card and pamphlet that has already been made (attached files). It should look professional and easy to read business. Email and phone number should be visible when the page loads. I do not want any forms for people to mess with. No "Contact Us" form or enter in email for newsletter. Customers will just be looking for this site to confirm we are professionals and have our business in order. OpenStreetMap: embedding map in webpage (like Google Maps) to where the workshop is located
Nice to have
• 2vask.com => this style of website would be more modern visually by integrating higher demands

```html
<!DOCTYPE html>
<html lang="en">
<head>
<meta charset="utf-8">
<title>Velmar Tech – Computer Repair, Service and Upgrades</title>
<link rel="stylesheet" href="https://fonts.googleapis.com/css2?family=Raleway:wght@400;600;800&family=Open+Sans:wght@400;600&display=swap">
<style>
:root{
  --blue:#2b8bd6;
  --blue-dark:#1f6fb0;
  --ink:#2b3440;
  --text:#6b7580;
  --pale:#e8f2fb;
  --header-bg:#eef1f4;
  --map-light:#d6e8f7;
  --map-deep:#9cc6ea;
  --footer:#2b2f34;
  --white:#ffffff;
}
*{margin:0;padding:0;box-sizing:border-box}
html,body{width:1200px;height:5324px;overflow:hidden}
body{font-family:"Open Sans",Arial,sans-serif;color:var(--text);background:var(--white)}
h1,h2,h3,.brand{font-family:"Raleway",Arial,sans-serif}

/* header */
.site-header{position:relative;height:680px;background:var(--header-bg);overflow:hidden}
.hero-photo{position:absolute;left:560px;top:0;width:640px;height:680px;background:linear-gradient(135deg,#d9dee3 0%,#b9c1c8 45%,#f2f2f2 100%)}
.brand{position:absolute;left:80px;top:120px;display:flex;align-items:center;gap:18px;font-weight:800;font-size:50px;color:var(--blue);letter-spacing:1px}
.brand-mark{width:40px;height:40px;background:var(--blue)}
.contact-lines{position:absolute;left:80px;top:320px}
.contact-lines .call{font-family:"Raleway",Arial,sans-serif;font-weight:600;font-size:26px;color:var(--ink);margin-bottom:22px}
.contact-lines .line{display:flex;align-items:center;gap:20px;font-family:"Raleway",Arial,sans-serif;font-weight:600;font-size:44px;color:var(--blue);margin-bottom:16px;white-space:nowrap}
.contact-lines svg{width:40px;height:40px;flex:0 0 40px}

/* welcome */
.welcome{height:310px;background:var(--blue);color:var(--white);text-align:center;padding:68px 260px 0}
.welcome h1{font-size:44px;font-weight:800;letter-spacing:1px;margin-bottom:26px}
.welcome p{font-size:17px;line-height:28px;opacity:.9}

/* services */
.service{position:relative;display:flex;align-items:center;padding:0 140px;gap:110px}
.service.alt{background:var(--pale);flex-direction:row-reverse;padding:0 140px 0 80px}
.service-art{flex:0 0 320px;height:270px;border-radius:6px}
.service-copy{flex:1}
.service h2{font-size:48px;font-weight:800;line-height:54px;text-transform:uppercase;color:var(--ink);margin-bottom:18px}
.service h2 .accent{color:var(--blue)}
.service p{font-size:17px;line-height:28px;max-width:500px}
.s1{height:390px}.s2{height:380px}.s3{height:420px}.s4{height:392px}.s5{height:388px}
.s6{height:400px}.s7{height:380px}.s8{height:380px}.s9{height:432px}
.art-people{background:linear-gradient(135deg,#cfd6dc,#8c98a4)}
.art-shield{background:linear-gradient(135deg,#d7e9f8,#6ea9dc)}
.art-devices{background:linear-gradient(135deg,#dfe3e8,#4c5a66)}
.art-upgrade{background:linear-gradient(135deg,#e4eef7,#5aa4e0)}
.art-migration{background:linear-gradient(135deg,#fdf0c8,#7fb6e6)}
.art-servers{background:linear-gradient(135deg,#eceff2,#9aa4ae)}
.art-tower{background:linear-gradient(135deg,#e6e9ec,#3d4550)}
.art-home{background:linear-gradient(135deg,#d8ecfb,#4f9ee0)}
.art-remote{background:linear-gradient(135deg,#eef1f4,#7a8592)}

/* contact */
.contact{position:relative;height:488px;background:var(--blue);overflow:hidden}
.contact h2{position:absolute;top:48px;width:100%;text-align:center;font-size:40px;font-weight:800;color:var(--white);letter-spacing:1px}
.location-map{position:absolute;left:100px;top:130px;width:1000px;height:330px;background:linear-gradient(135deg,var(--map-light),var(--map-deep));border-radius:4px}
.contact-card{position:absolute;left:130px;top:160px;width:290px;height:200px;background:var(--white);padding:40px 30px;box-shadow:0 6px 18px rgba(0,0,0,.12)}
.contact-card h3{font-size:22px;font-weight:800;color:var(--blue);margin-bottom:14px}
.contact-card p{font-size:15px;line-height:24px}

/* footer */
.site-footer{position:relative;height:284px;background:var(--footer);color:#c9ced3}
.footer-row{position:absolute;top:88px;left:130px;right:50px;display:flex;align-items:center;font-size:17px}
.footer-row .item{display:flex;align-items:center;gap:14px;margin-right:200px}
.footer-row svg{width:24px;height:24px}
.social{margin-left:auto;display:flex;gap:20px}
.social span{width:40px;height:40px;border-radius:50%;background:#3a3f45;display:block}
.footer-rule{position:absolute;top:160px;left:40px;right:40px;height:1px;background:#41464c}
.footer-brand{position:absolute;top:190px;width:100%;display:flex;justify-content:center;align-items:center;gap:10px;font-size:26px;font-weight:800;color:var(--blue)}
.footer-brand .brand-mark{width:20px;height:20px}
.copyright{position:absolute;top:246px;width:100%;text-align:center;font-size:14px}
.copyright b{color:var(--blue);font-weight:600}
</style>
</head>
<body>

<header class="site-header">
  <div class="hero-photo" role="img" aria-label="Photo of a technician working inside an open computer tower"></div>
  <div class="brand"><span class="brand-mark"></span>VELMAR TECH</div>
  <div class="contact-lines">
    <div class="call">Call Us When You Need Us</div>
    <div class="line">
      <svg viewBox="0 0 24 24" fill="none" stroke="currentColor" stroke-width="2"><path d="M5 3h4l2 5-2.5 1.5a11 11 0 0 0 6 6L16 13l5 2v4a2 2 0 0 1-2 2A17 17 0 0 1 3 5a2 2 0 0 1 2-2z"/></svg>
      555-014-2298
    </div>
    <div class="line">
      <svg viewBox="0 0 24 24" fill="none" stroke="currentColor" stroke-width="2"><rect x="2" y="4" width="20" height="16" rx="2"/><path d="M2 6l10 7 10-7"/></svg>
      help@velmartech.com
    </div>
  </div>
</header>

<section class="welcome">
  <h1>WELCOME TO VELMAR TECH</h1>
  <p>We fix, upgrade and look after computers for homes and small offices. Every job is handled by certified technicians who explain the work in plain words, quote a fair price up front and finish on time, so your devices keep running smoothly.</p>
</section>

<section class="service s1">
  <div class="service-art art-people" role="img" aria-label="Photo of a smiling technician holding a laptop"></div>
  <div class="service-copy">
    <h2><span class="accent">Honest</span> Services</h2>
    <p>Our certified technicians never push extra purchases. We only recommend upgrades or products you truly need, and we always talk you through the options first. That is why our customers come back to us.</p>
  </div>
</section>

<section class="service alt s2">
  <div class="service-art art-shield" role="img" aria-label="Illustration of a robot holding a shield over a laptop"></div>
  <div class="service-copy">
    <h2><span class="accent">Malware /</span>Virus<br>Removal</h2>
    <p>Infections can come from many places and sometimes without you noticing. We clean your system back to top shape and show you how to avoid trouble in the future, which is better than any antivirus alone.</p>
  </div>
</section>

<section class="service s3">
  <div class="service-art art-devices" role="img" aria-label="Illustration of a desktop monitor and laptop with repair tools"></div>
  <div class="service-copy">
    <h2><span class="accent">PC/Desktop/Laptop</span><br>Hardware Repair</h2>
    <p>Has your machine stopped booting or started making strange noises? Our technicians will find the faulty part, suggest the best value replacement and return it good as new.</p>
  </div>
</section>

<section class="service alt s4">
  <div class="service-art art-upgrade" role="img" aria-label="Illustration of a hand holding a stopwatch beside a screen"></div>
  <div class="service-copy">
    <h2><span class="accent">Upgrades</span></h2>
    <p>A new machine is not always the answer. Extra memory, a faster drive or the latest system update can give your current computer years of extra life. We can make the upgrade painless for you.</p>
  </div>
</section>

<section class="service s5">
  <div class="service-art art-migration" role="img" aria-label="Illustration of folders moving between two computer screens"></div>
  <div class="service-copy">
    <h2><span class="accent">Data</span> Migration</h2>
    <p>Got a new computer and need your old one moved over? We transfer your files, photos, bookmarks, email accounts and settings so your new machine feels familiar from day one.</p>
  </div>
</section>

<section class="service alt s6">
  <div class="service-art art-servers" role="img" aria-label="Illustration of stacked hard drives with a red rescue cross"></div>
  <div class="service-copy">
    <h2><span class="accent">Data</span> Rescue</h2>
    <p>Drive failed or files deleted by mistake? Don't panic. We can often recover lost documents, photos and records from damaged drives. If we can't get your files back, you won't be charged.</p>
  </div>
</section>

<section class="service s7">
  <div class="service-art art-tower" role="img" aria-label="Illustration of a computer tower and monitor with a wrench"></div>
  <div class="service-copy">
    <h2><span class="accent">Tune</span> Ups</h2>
    <p>Over time systems slow down from unneeded startup programs, leftover files and clutter. A thorough tune up clears the junk and gets your computer running at peak performance again.</p>
  </div>
</section>

<section class="service alt s8">
  <div class="service-art art-home" role="img" aria-label="Illustration of a house connected to a router and printer"></div>
  <div class="service-copy">
    <h2><span class="accent">In Home</span> Installation</h2>
    <p>We come to you to set up wireless networking, printers, cables and new devices, and we make sure everything works together before we leave your home.</p>
  </div>
</section>

<section class="service s9">
  <div class="service-art art-remote" role="img" aria-label="Illustration of two computers linked for remote support"></div>
  <div class="service-copy">
    <h2><span class="accent">Remote</span> Support</h2>
    <p>Many problems can be solved without a visit. With your permission we connect securely to your computer, fix the issue while you watch and save you a trip to the shop.</p>
  </div>
</section>

<section class="contact">
  <h2>CONTACT US</h2>
  <div class="location-map" role="img" aria-label="Street map showing where the Velmar Tech workshop is located"></div>
  <div class="contact-card">
    <h3>VELMAR TECH</h3>
    <p>Friendly repairs for home and small business.</p>
  </div>
</section>

<footer class="site-footer">
  <div class="footer-row">
    <div class="item">
      <svg viewBox="0 0 24 24" fill="none" stroke="currentColor" stroke-width="2"><path d="M5 3h4l2 5-2.5 1.5a11 11 0 0 0 6 6L16 13l5 2v4a2 2 0 0 1-2 2A17 17 0 0 1 3 5a2 2 0 0 1 2-2z"/></svg>
      555-014-2298
    </div>
    <div class="item">
      <svg viewBox="0 0 24 24" fill="none" stroke="currentColor" stroke-width="2"><rect x="2" y="4" width="20" height="16" rx="2"/><path d="M2 6l10 7 10-7"/></svg>
      help@velmartech.com
    </div>
    <div class="social"><span></span><span></span></div>
  </div>
  <div class="footer-rule"></div>
  <div class="footer-brand"><span class="brand-mark"></span>VELMAR TECH</div>
  <p class="copyright">© 2025 <b>VELMAR TECH</b>. All Rights Reserved</p>
</footer>

</body>
</html>
```